eBook opt in for website

I write short ebooks (2500 words) to give free as an opt in. I need a cover design with block headers within the pages to highlight the specifics sections for PDF.
Book Title:
Bridgeway Mentoring
Sharpen Your Crew Guidance Using Five Simple Habits
I would like to see a design for the front cover that would emphasize a leader's personal growth to team.
The color that comes to mind is blue.
I do have a Brand Design and Icon if you need it.

Leaders with Team Responsibility
Business Consultant

```html
<!DOCTYPE html>
<html lang="en">
<head>
<meta charset="UTF-8">
<title>Bridgeway Mentoring – eBook Cover</title>
<link rel="stylesheet" href="https://fonts.googleapis.com/css2?family=Bebas+Neue&family=Josefin+Slab:ital,wght@0,300;0,400;1,700&display=swap">
<style>
  :root {
    --page-bg: #f1f1f1;
    --band-deep: #34a3d6;
    --band-light: #68bbe1;
    --title-cream: #fdfcc8;
    --text-white: #ffffff;
    --accent-gold: #f7c21a;
  }
  * { margin: 0; padding: 0; box-sizing: border-box; }
  html, body {
    width: 1200px;
    height: 1000px;
    overflow: hidden;
    background: var(--page-bg);
  }
  .canvas {
    position: relative;
    width: 1200px;
    height: 1000px;
  }
  .cover {
    position: absolute;
    left: 297px;
    top: 37px;
    width: 605px;
    height: 806px;
    background: var(--band-deep);
    overflow: hidden;
  }
  .cover__brand {
    position: absolute;
    top: 0;
    left: 0;
    width: 100%;
    height: 221px;
    display: flex;
    align-items: center;
    justify-content: center;
    gap: 12px;
  }
  .brand__dot {
    width: 22px;
    height: 22px;
    border: 2px solid var(--text-white);
    border-radius: 50%;
  }
  .brand__name {
    font-family: "Josefin Slab", serif;
    font-weight: 400;
    font-size: 26px;
    letter-spacing: 1px;
    color: var(--text-white);
  }
  .cover__feature {
    position: absolute;
    top: 221px;
    left: 0;
    width: 100%;
    height: 364px;
    background: linear-gradient(168deg, var(--band-light) 0%, var(--band-light) 22%, var(--band-deep) 45%, var(--band-deep) 70%, var(--band-light) 88%);
  }
  .cover__title {
    position: absolute;
    top: 221px;
    left: 0;
    width: 100%;
    height: 364px;
    display: flex;
    flex-direction: column;
    justify-content: center;
    align-items: center;
    font-family: "Bebas Neue", sans-serif;
    font-weight: 400;
    font-size: 142px;
    line-height: 118px;
    letter-spacing: 2px;
    color: var(--title-cream);
    text-align: center;
    padding-top: 8px;
  }
  .cover__subtitle {
    position: absolute;
    top: 585px;
    left: 0;
    width: 100%;
    height: 221px;
    display: flex;
    flex-direction: column;
    justify-content: center;
    align-items: center;
    font-family: "Josefin Slab", serif;
    font-weight: 300;
    font-size: 38px;
    line-height: 54px;
    letter-spacing: 1px;
    color: var(--text-white);
    text-align: center;
  }
  .subtitle__accent {
    font-weight: 700;
    font-style: italic;
    color: var(--accent-gold);
  }
</style>
</head>
<body>
  <main class="canvas">
    <section class="cover">
      <header class="cover__brand">
        <span class="brand__dot"></span>
        <span class="brand__name">Clearpath Coaching</span>
      </header>
      <div class="cover__feature" role="img" aria-label="Silhouette illustration of two hands reaching toward each other in a handshake, in soft blue tones"></div>
      <h1 class="cover__title">
        <span>Bridgeway</span>
        <span>Mentoring</span>
      </h1>
      <p class="cover__subtitle">
        <span>Sharpen Your</span>
        <span>Crew Guidance</span>
        <span>Using <span class="subtitle__accent">Five</span> Simple Habits</span>
      </p>
    </section>
  </main>
</body>
</html>
```